Brennick Works 'Velvet Glaze' Label

We need a label for our new Exterior Ceramic Coat spray. It is going to be called Velvet Glaze. This label needs to exude a premium feel yet also retain elements of FUN. This product when applied to a vehicle exterior creates a highly durable barrier and incredible shine. Ceramic coats are a popular way to make your paint turn heads! - and ours is the best. We'd like to see designs that match our line and previous projects but we want this label to stick out a little like its something special. Oranges, Reds, Silver, White, could all be great ideas, we dont have a set color or fragrance for this yet so all ideas are welcome!

```html
<!DOCTYPE html>
<html lang="en">
<head>
<meta charset="utf-8">
<title>Velvet Glaze – Exterior Ceramic Coat Spray Label</title>
<link rel="stylesheet" href="https://fonts.googleapis.com/css2?family=Jost:wght@500;600;700&display=swap">
<style>
  :root {
    --brand-red: #c11f2f;
    --brand-red-deep: #a8172a;
    --brand-red-soft: #dd5a67;
    --label-white: #ffffff;
    --ink: #111111;
  }
  html, body {
    margin: 0;
    padding: 0;
    width: 748px;
    height: 1200px;
    overflow: hidden;
    background: var(--label-white);
  }
  .label {
    position: relative;
    width: 748px;
    height: 1200px;
    overflow: hidden;
    font-family: "Jost", "Futura", sans-serif;
    color: var(--ink);
    background: var(--label-white);
  }
  .swirl-field {
    position: absolute;
    inset: 0;
    background:
      radial-gradient(ellipse 220px 140px at 18% 10%, rgba(255,255,255,0.55), transparent 70%),
      radial-gradient(ellipse 260px 160px at 80% 14%, rgba(255,255,255,0.45), transparent 70%),
      radial-gradient(ellipse 240px 150px at 25% 50%, rgba(255,255,255,0.45), transparent 70%),
      radial-gradient(ellipse 220px 170px at 78% 56%, rgba(255,255,255,0.4), transparent 70%),
      radial-gradient(ellipse 230px 150px at 15% 90%, rgba(255,255,255,0.45), transparent 70%),
      radial-gradient(ellipse 230px 150px at 88% 92%, rgba(255,255,255,0.45), transparent 70%),
      linear-gradient(160deg, var(--brand-red) 0%, var(--brand-red-soft) 35%, var(--brand-red-deep) 60%, var(--brand-red) 100%);
  }
  .band {
    position: absolute;
    left: 0;
    right: 0;
    display: flex;
    flex-direction: column;
    align-items: center;
    justify-content: center;
    text-align: center;
  }
  .band--title {
    top: 218px;
    height: 262px;
    background: linear-gradient(to bottom,
      rgba(255,255,255,0) 0%,
      var(--label-white) 23%,
      var(--label-white) 78%,
      rgba(255,255,255,0) 100%);
  }
  .band--benefits {
    top: 672px;
    height: 240px;
    background: linear-gradient(to bottom,
      rgba(255,255,255,0) 0%,
      var(--label-white) 24%,
      var(--label-white) 84%,
      rgba(255,255,255,0) 100%);
  }
  .product-name {
    margin: 0;
    font-size: 60px;
    font-weight: 600;
    letter-spacing: 2px;
    line-height: 1;
    margin-top: 8px;
  }
  .product-type {
    margin: 22px 0 0;
    font-size: 32px;
    font-weight: 600;
    letter-spacing: 0.5px;
    line-height: 1;
  }
  .benefits {
    list-style: none;
    margin: 22px 0 0;
    padding: 0;
    font-size: 41px;
    font-weight: 600;
    line-height: 70px;
  }
  .volume-badge {
    position: absolute;
    left: 294px;
    top: 976px;
    width: 160px;
    height: 160px;
    border-radius: 50%;
    display: flex;
    align-items: center;
    justify-content: center;
    background: radial-gradient(circle, var(--label-white) 0%, var(--label-white) 52%, rgba(255,255,255,0) 72%);
    font-size: 31px;
    font-weight: 600;
  }
</style>
</head>
<body>
  <main class="label">
    <div class="swirl-field" role="img" aria-label="Red and white marbled swirl pattern"></div>

    <header class="band band--title">
      <h1 class="product-name">VELVET GLAZE</h1>
      <p class="product-type">Exterior Ceramic Coat spray</p>
    </header>

    <section class="band band--benefits">
      <ul class="benefits">
        <li>highly durable barrier</li>
        <li>incredible shine</li>
      </ul>
    </section>

    <div class="volume-badge">200ml</div>
  </main>
</body>
</html>
```